New LLC consulting company needs a business card design

I need a business card design for new company in Alexandria Virginia called TK Verdant Consulting LLC. The company is focused on consulting for defense and national security issues with expertise in nuclear and space topics. I would like to see designs that are simple and I am open to colors except for brown.

Target Market(s)

All businesses that are seeking consulting help

Industry/Entity Type

Consulting

Contact Information for Business Card

Name of company - TK Verdant Consulting LLC; name (Delia Hawke) President; email: hawkedr41@mailbox-example.net; Phone: 555-271-9043

Requirements
Must have
• The details described above
Nice to have
• I'm open to all ideas
Should not have
• No brown

```html
<!DOCTYPE html>
<html lang="en">
<head>
<meta charset="utf-8">
<title>TK Verdant Consulting LLC – Business Card</title>
<link href="https://fonts.googleapis.com/css2?family=Playfair+Display:wght@600;700&family=Montserrat:wght@300;400;500&family=Outfit:wght@500;600&display=swap" rel="stylesheet">
<style>
  :root {
    --forest: #283322;
    --cream: #f0e7de;
    --gold: #c6a468;
    --gold-deep: #a8864f;
    --ink: #283322;
    --band: linear-gradient(90deg, #a88b5a 0%, #9d7f51 18%, #8a6c44 28%, #b59564 42%, #e3bc7c 56%, #f0c887 63%, #ddb476 76%, #b99660 88%, #8d7046 100%);
  }
  * { box-sizing: border-box; margin: 0; padding: 0; }
  html, body { width: 1071px; height: 1200px; overflow: hidden; background: #ffffff; }
  body { position: relative; }

  .card { position: absolute; left: 150px; width: 742px; height: 433px; overflow: hidden; }
  .card--front { top: 105px; background: var(--forest); }
  .card--back { top: 623px; background: var(--cream); }

  .gold-band { position: absolute; left: 0; bottom: 0; width: 100%; height: 61px; background: var(--band); }

  .wordmark {
    position: absolute; left: 0; width: 100%; text-align: center;
    font-family: "Playfair Display", Georgia, serif; font-weight: 700;
    font-size: 52px; line-height: 1; color: var(--gold);
  }
  .entity {
    position: absolute; left: 0; width: 100%; text-align: center;
    font-family: "Playfair Display", Georgia, serif; font-weight: 600;
    font-size: 13px; letter-spacing: 0.62em; text-indent: 0.62em;
  }

  .card--front .wordmark { top: 158px; }
  .card--front .entity { top: 214px; color: var(--cream); }
  .tagline {
    position: absolute; left: 0; top: 280px; width: 100%; text-align: center;
    font-family: "Montserrat", Arial, sans-serif; font-weight: 400;
    font-size: 12.5px; line-height: 16.5px; letter-spacing: 0.2em; color: var(--gold);
  }

  .name-panel { position: absolute; left: 0; top: 0; width: 309px; height: 372px; background: var(--forest); }
  .person-name {
    position: absolute; left: 87px; top: 127px;
    font-family: "Montserrat", Arial, sans-serif; font-weight: 300;
    font-size: 36px; line-height: 41px; letter-spacing: 0.26em; color: var(--gold);
  }
  .person-role {
    position: absolute; left: 89px; top: 223px;
    font-family: "Montserrat", Arial, sans-serif; font-weight: 400;
    font-size: 18px; letter-spacing: 0.2em; color: var(--cream);
  }

  .brand-panel { position: absolute; left: 309px; top: 0; width: 433px; height: 372px; }
  .brand-panel .wordmark { top: 137px; font-size: 51px; }
  .brand-panel .entity { top: 190px; color: var(--ink); }

  .contact { position: absolute; left: 64px; display: flex; align-items: center; color: var(--ink); font-family: "Outfit", Arial, sans-serif; }
  .contact svg { flex: none; }
  .contact--phone { top: 248px; font-size: 33px; font-weight: 600; }
  .contact--phone svg { margin-right: 12px; }
  .contact--email { top: 305px; font-size: 20px; font-weight: 500; }
  .contact--email svg { margin-right: 10px; }
</style>
</head>
<body>

<section class="card card--front">
  <div class="wordmark">TK VERDANT</div>
  <div class="entity">CONSULTING LLC</div>
  <p class="tagline">CONSULTING ON DEFENSE AND NATIONAL SECURITY ISSUES<br>EXPERTISE IN NUCLEAR AND SPACE TOPICS.</p>
  <div class="gold-band"></div>
</section>

<section class="card card--back">
  <div class="name-panel">
    <div class="person-name">DELIA<br>HAWKE</div>
    <div class="person-role">PRESIDENT</div>
  </div>
  <div class="brand-panel">
    <div class="wordmark">TK VERDANT</div>
    <div class="entity">CONSULTING LLC</div>
    <div class="contact contact--phone">
      <svg width="26" height="34" viewBox="0 0 26 34" aria-hidden="true">
        <path d="M6 2 L10 9 Q11 11 9 12.5 L7.5 13.5 Q8 20 14 26 L15.5 25 Q17.5 24 19 25.5 L24 30.5 Q24.5 32 22.5 32.5 Q17 34 11 27 Q3 18 2.5 9 Q2.5 3.5 6 2 Z" fill="none" stroke="var(--gold-deep)" stroke-width="1.4" stroke-linejoin="round"/>
      </svg>
      <span>555-271-9043</span>
    </div>
    <div class="contact contact--email">
      <svg width="31" height="22" viewBox="0 0 31 22" aria-hidden="true">
        <rect x="1" y="1" width="29" height="20" fill="none" stroke="var(--gold-deep)" stroke-width="1.6"/>
        <path d="M1 1 L15.5 13 L30 1 M1 21 L12 10.5 M30 21 L19 10.5" fill="none" stroke="var(--gold-deep)" stroke-width="1.6"/>
      </svg>
      <span>hawkedr41@mailbox-example.net</span>
    </div>
  </div>
  <div class="gold-band"></div>
</section>

</body>
</html>
```